New Cancer Patient
Handbook & Folder
New Cancer Patient  - Health
Creative Brief
Health
New cancer patients
Feel free to message with ANY questions! This is a very special project, I simply do not have the time to devote to it that it requires right now
belqodran belqodran
the size of the booklet will be same or else, plz tell?. and how many pages will be there...and folder will be A4 or what type plz clear?...thx a lot

```html
<!DOCTYPE html>
<html lang="en">
<head>
<meta charset="utf-8">
<title>New Patient Handbook – Spread</title>
<link rel="stylesheet" href="https://fonts.googleapis.com/css2?family=Open+Sans:wght@400;600&family=Great+Vibes&display=swap">
<style>
  :root {
    --backdrop: #8c8c8c;
    --paper: #ffffff;
    --paper-shade: #f1f2f3;
    --ink: #5c6166;
    --ink-soft: #8d9296;
    --brand-blue: #1d7cc4;
    --brand-blue-dark: #135a92;
    --leader: #c9cdd0;
    --photo-warm-light: #cbbfb0;
    --photo-warm-mid: #a08770;
    --photo-warm-dark: #6f5a48;
  }
  * { box-sizing: border-box; margin: 0; padding: 0; }
  html, body { width: 1200px; height: 526px; overflow: hidden; }
  body {
    background: var(--backdrop);
    font-family: "Open Sans", Arial, sans-serif;
    color: var(--ink);
    position: relative;
  }
  .spread {
    position: absolute;
    left: 40px; top: 40px;
    width: 1120px; height: 440px;
    display: flex;
    background: var(--paper);
    border-bottom: 9px solid var(--brand-blue);
  }
  .page { position: relative; width: 560px; height: 100%; display: flex; }
  .page--left { border-right: 1px solid #dfe2e4; }

  /* Left page, welcome column */
  .welcome { width: 200px; display: flex; flex-direction: column; }
  .welcome__photo {
    height: 190px;
    background: linear-gradient(180deg, var(--photo-warm-light) 0%, var(--photo-warm-mid) 100%);
  }
  .welcome__body { padding: 18px 18px 0; font-size: 9px; line-height: 1.6; }
  .welcome__signature {
    display: block;
    font-family: "Great Vibes", cursive;
    font-size: 22px; line-height: 1.2;
    color: #444;
    white-space: nowrap;
    margin-top: 70px;
  }
  .welcome__role { display: block; font-size: 8px; color: var(--ink-soft); margin-top: 2px; }

  /* Left page, contents */
  .contents {
    flex: 1;
    background: var(--paper-shade);
    padding: 44px 34px 0 34px;
  }
  .contents__list { list-style: none; }
  .contents__item {
    display: flex; align-items: baseline;
    font-size: 10px; line-height: 2.15;
  }
  .contents__leader { flex: 1; border-bottom: 1px dotted var(--leader); margin: 0 6px; }
  .contents__page { color: var(--ink-soft); }

  /* Right page */
  .treatment__photo {
    width: 320px;
    background: linear-gradient(180deg, var(--photo-warm-mid) 0%, var(--photo-warm-dark) 100%);
  }
  .about { flex: 1; padding: 26px 22px 0; }
  .brand { display: flex; align-items: center; gap: 7px; margin-bottom: 22px; }
  .brand__dot { width: 12px; height: 12px; border-radius: 50%; background: var(--brand-blue); flex: none; }
  .brand__name { font-size: 10px; font-weight: 600; color: var(--brand-blue-dark); }
  .contact { list-style: none; margin-bottom: 20px; }
  .contact__item { display: flex; align-items: center; gap: 7px; font-size: 8.5px; line-height: 2; color: var(--brand-blue); }
  .contact__icon { width: 11px; height: 11px; flex: none; }
  .about__text { font-size: 9px; line-height: 1.6; }
</style>
</head>
<body>
  <main class="spread">
    <section class="page page--left">
      <div class="welcome">
        <div class="welcome__photo" role="img" aria-label="Photo of a treatment room with a staff member beside equipment"></div>
        <div class="welcome__body">
          <p>Welcome to our center. We know this is a difficult time, and our team is here to guide you through every step of your treatment with care, respect and clear answers.</p>
          <span class="welcome__signature">Daniel Rowe, MD</span>
          <span class="welcome__role">Medical Director</span>
        </div>
      </div>
      <nav class="contents" aria-label="Contents">
        <ul class="contents__list">
          <li class="contents__item"><span>Welcome Letter</span><span class="contents__leader"></span><span class="contents__page">1</span></li>
          <li class="contents__item"><span>About Our Center</span><span class="contents__leader"></span><span class="contents__page">2</span></li>
          <li class="contents__item"><span>Your Care Team</span><span class="contents__leader"></span><span class="contents__page">3</span></li>
          <li class="contents__item"><span>Understanding Your Diagnosis</span><span class="contents__leader"></span><span class="contents__page">4</span></li>
          <li class="contents__item"><span>Treatment Options</span><span class="contents__leader"></span><span class="contents__page">5</span></li>
          <li class="contents__item"><span>Radiation Therapy</span><span class="contents__leader"></span><span class="contents__page">6</span></li>
          <li class="contents__item"><span>Chemotherapy Basics</span><span class="contents__leader"></span><span class="contents__page">7</span></li>
          <li class="contents__item"><span>Managing Side Effects</span><span class="contents__leader"></span><span class="contents__page">8</span></li>
          <li class="contents__item"><span>Nutrition Guide</span><span class="contents__leader"></span><span class="contents__page">9</span></li>
          <li class="contents__item"><span>Emotional Support</span><span class="contents__leader"></span><span class="contents__page">10</span></li>
          <li class="contents__item"><span>Financial Resources</span><span class="contents__leader"></span><span class="contents__page">11</span></li>
          <li class="contents__item"><span>Questions To Ask</span><span class="contents__leader"></span><span class="contents__page">12</span></li>
          <li class="contents__item"><span>Appointment Calendar</span><span class="contents__leader"></span><span class="contents__page">13</span></li>
          <li class="contents__item"><span>Notes</span><span class="contents__leader"></span><span class="contents__page">14</span></li>
        </ul>
      </nav>
    </section>

    <section class="page page--right">
      <div class="treatment__photo" role="img" aria-label="Photo of a patient lying on a radiation therapy machine"></div>
      <div class="about">
        <div class="brand">
          <span class="brand__dot"></span>
          <span class="brand__name">Northvale Cancer Institute</span>
        </div>
        <ul class="contact">
          <li class="contact__item">
            <svg class="contact__icon" viewBox="0 0 12 12"><circle cx="6" cy="6" r="6" fill="#1d7cc4"/><path d="M4 3.2l1 1.6-.6.7c.4.9 1 1.5 1.9 1.9l.7-.6 1.6 1-.5 1c-2.6-.2-4.4-2-4.6-4.6z" fill="#fff"/></svg>
            <span>555-0142</span>
          </li>
          <li class="contact__item">
            <svg class="contact__icon" viewBox="0 0 12 12"><circle cx="6" cy="6" r="6" fill="#1d7cc4"/><rect x="3" y="4" width="6" height="4.2" fill="none" stroke="#fff" stroke-width=".8"/><path d="M3 4l3 2.3L9 4" fill="none" stroke="#fff" stroke-width=".8"/></svg>
            <span>info@northvale.org</span>
          </li>
          <li class="contact__item">
            <svg class="contact__icon" viewBox="0 0 12 12"><circle cx="6" cy="6" r="6" fill="#1d7cc4"/><circle cx="6" cy="6" r="3" fill="none" stroke="#fff" stroke-width=".8"/><path d="M3 6h6M6 3c-1.4 1.8-1.4 4.2 0 6M6 3c1.4 1.8 1.4 4.2 0 6" fill="none" stroke="#fff" stroke-width=".6"/></svg>
            <span>northvale.org</span>
          </li>
        </ul>
        <p class="about__text">Our institute offers modern radiation and medical oncology under one roof. This handbook explains what to expect, who to call, and how to prepare for each visit. Keep it with you and bring it to appointments.</p>
      </div>
    </section>
  </main>
</body>
</html>
```